Brightpath Letterhead

We would like a letterhead for our company. I have uploaded our logo.

Brightpath Ridge Consulting
1450 W Corliss Ave Ste 310
Garland, TX 75040
833-517-2906

```html
<!DOCTYPE html>
<html lang="en">
<head>
<meta charset="utf-8">
<title>Brightpath Letterhead</title>
<link href="https://fonts.googleapis.com/css2?family=Montserrat:ital,wght@0,400;0,600;0,700;1,400&family=Arimo:wght@700&display=swap" rel="stylesheet">
<style>
  :root {
    --backdrop: #e6e9eb;
    --paper: #ffffff;
    --sidebar: #3e6d84;
    --brand-blue: #3a6a80;
    --ink: #3b3b3b;
    --ink-soft: #4a4a4a;
    --signature-tone: #eef3ef;
  }
  * { margin: 0; padding: 0; box-sizing: border-box; }
  html, body { width: 1200px; height: 1200px; overflow: hidden; background: var(--backdrop); }
  .canvas { position: relative; width: 1200px; height: 1200px; }
  .letterhead {
    position: absolute; left: 167px; top: 40px; width: 865px; height: 1120px;
    background: var(--paper); overflow: hidden;
    font-family: "Montserrat", sans-serif; color: var(--ink);
    box-shadow: 0 6px 24px rgba(0,0,0,0.12);
  }
  .sidebar { position: absolute; left: 0; top: 0; width: 163px; height: 100%; background: var(--sidebar); }
  .brand {
    position: absolute; left: 192px; top: 58px; display: flex; align-items: center; gap: 12px;
  }
  .brand-dot { width: 34px; height: 34px; border-radius: 50%; background: var(--brand-blue); }
  .brand-name {
    font-family: "Montserrat", sans-serif; font-weight: 600; font-size: 22px;
    letter-spacing: 2px; text-transform: uppercase; color: var(--brand-blue); line-height: 1.15;
  }
  .date { position: absolute; left: 209px; top: 294px; font-weight: 600; font-size: 15px; }
  .recipient { position: absolute; left: 209px; top: 350px; font-size: 15px; line-height: 22px; }
  .recipient .label { font-weight: 400; }
  .recipient .name { font-weight: 700; }
  .recipient .role { font-style: italic; }
  .body-copy {
    position: absolute; left: 209px; top: 459px; width: 552px;
    font-size: 14.5px; line-height: 23.7px; letter-spacing: 0.35px;
    text-align: justify; color: var(--ink-soft);
  }
  .body-copy p { margin-bottom: 18.5px; }
  .signoff { position: absolute; right: 103px; top: 808px; text-align: right; font-size: 15px; }
  .signature {
    position: absolute; right: 123px; top: 836px; width: 120px; height: 44px;
    background: var(--signature-tone); border-radius: 4px;
  }
  .signer { position: absolute; left: 657px; top: 882px; font-weight: 700; font-size: 15.5px; }
  .contact {
    position: absolute; right: 32px; top: 1028px; text-align: right;
    font-family: "Arimo", sans-serif; font-weight: 700; font-size: 12.5px; color: var(--brand-blue);
  }
  .contact-line { display: flex; justify-content: flex-end; align-items: center; gap: 8px; height: 25.5px; }
  .contact-icon { width: 14px; height: 14px; }
  .icon-spacer { width: 14px; }
</style>
</head>
<body>
<div class="canvas">
  <main class="letterhead">
    <aside class="sidebar"></aside>

    <header class="brand">
      <span class="brand-dot"></span>
      <span class="brand-name">Brightpath Ridge<br>Consulting</span>
    </header>

    <p class="date">Date, 22 February 2022</p>

    <div class="recipient">
      <div class="label">To:</div>
      <div class="name">Daniel Reyes</div>
      <div class="role">Chief Officer</div>
    </div>

    <section class="body-copy">
      <p>Lorem ipsum dolor sit amet, consectetur adipiscing elit. Duis auctor sem vel metus interdum porta. Duis consequat bibendum felis eget cursus. Nulla eget purus vehicula ipsum finibus egestas. Nullam ligula ipsum, mollis sed gravida vitae, maximus eu dolor. Morbi luctus sem a congue consectetur.</p>
      <p>Orci varius natoque penatibus et magnis dis parturient montes, nascetur ridiculus mus. Vestibulum congue eros auctor, ullamcorper libero blandit, tempor tellus. Proin vitae tellus et nunc fringilla lacinia. Sed augue erat, facilisis laoreet velit a, convallis mattis nunc. Nunc sagittis ligula vitae sollicitudin sollicitudin.</p>
      <p>Nulla facilisi. Nulla quis odio vitae purus aliquam fermentum ut nec diam. Fusce sed velit ultrices, aliquam augue ut, sollicitudin orci.</p>
    </section>

    <p class="signoff">Kind Regards</p>
    <div class="signature" role="img" aria-label="Handwritten signature of Daniel Reyes"></div>
    <p class="signer">Daniel Reyes</p>

    <footer class="contact">
      <div class="contact-line">
        <span>1450 W Corliss Ave Ste 310</span>
        <svg class="contact-icon" viewBox="0 0 14 14" aria-hidden="true">
          <circle cx="7" cy="7" r="6" fill="none" stroke="currentColor" stroke-width="1.8"/>
          <circle cx="7" cy="6" r="2" fill="currentColor"/>
        </svg>
      </div>
      <div class="contact-line">
        <span>Garland, TX 75040</span><span class="icon-spacer"></span>
      </div>
      <div class="contact-line">
        <span>833-517-2906</span>
        <svg class="contact-icon" viewBox="0 0 14 14" aria-hidden="true">
          <circle cx="7" cy="7" r="7" fill="currentColor"/>
          <path d="M4.6 3.8 L6 3.6 L6.6 5.4 L5.8 6.1 Q6.5 7.7 8 8.3 L8.7 7.5 L10.4 8.1 L10.2 9.5 Q9.6 10.4 8.4 10.1 Q4.6 8.9 3.9 5.3 Q3.8 4.3 4.6 3.8 Z" fill="#ffffff"/>
        </svg>
      </div>
    </footer>
  </main>
</div>
</body>
</html>
```